Emergency Dental Referral Company

I need a brochure to advertise my business to prospective dentists that may want to join or to dentists that may want to use this for their own patients. I also need to advertise this brochure to ER physicians who see many dental emergencies. This brochure is meant to be dual purpose: advertise our company and services to the ER physicians who then hand out the brochures to the dental emergency patients in pain. See our website for further details at www.molarquickfix.com

I will also be attaching our logo design.

Target Market(s)

Emergency Room physicians and other medical personnel who will distribute these brochures to patients in dental pain and dental emergencies

Industry/Entity Type

Business

Font styles to use
Serif
Sans Serif

Requirements
Must have
• Must be simple! Must have a call to action- inspiration to go to website. Highlight our guarantee that states "If you are not seen by a dentist in 24 hours or less, you will receive your money back. Emphasis on the logo. Must discuss how we find a dentist in your zip code in three easy steps.
• For the color- please make similar to our website of www.molarquickfix.com
Nice to have
• Would like to state that this service can see patients at any hour of the day.
Should not have
• no contact information besides the URL. www.molarquickfix.com

```html
<!DOCTYPE html>
<html lang="en">
<head>
<meta charset="utf-8">
<title>Brochure Inside Spread</title>
<link rel="stylesheet" href="https://fonts.googleapis.com/css2?family=Source+Sans+3:wght@400;700&family=Tinos&display=swap">
<style>
  :root {
    --brand-blue: #0a6fbd;
    --body-grey: #444444;
    --frame-line: #333333;
    --label-brown: #6e3b0c;
    --page-bg: #ffffff;
  }
  * { margin: 0; padding: 0; box-sizing: border-box; }
  html, body {
    width: 1200px; height: 1000px; overflow: hidden;
    background: var(--page-bg);
  }
  .canvas { position: relative; width: 1200px; height: 1000px; }
  .spread {
    position: absolute; left: 83px; top: 65px;
    width: 1035px; height: 732px;
    border: 1px solid var(--frame-line);
  }
  .heading {
    position: absolute;
    font-family: "Source Sans 3", "Myriad Pro", sans-serif;
    font-weight: 700; font-size: 54px; line-height: 1;
    color: var(--brand-blue);
    text-decoration: underline;
    text-decoration-thickness: 3px;
    text-underline-offset: 5px;
    white-space: nowrap;
    letter-spacing: -0.3px;
  }
  .heading--mission { left: 110px; width: 290px; text-align: center; top: 10px; }
  .heading--todo { left: 60px; width: 335px; text-align: center; top: 250px; }
  .heading--right-a { left: 537px; top: 10px; }
  .heading--right-b { left: 537px; top: 268px; }
  .copy {
    position: absolute;
    font-family: "Source Sans 3", "Myriad Pro", sans-serif;
    font-size: 13.6px; line-height: 17.6px;
    color: var(--body-grey);
    letter-spacing: -0.15px;
  }
  .copy--mission { left: 10px; top: 69px; width: 497px; text-align: justify; text-align-last: justify; }
  .copy--right { left: 527px; width: 495px; hyphens: auto; }
  .copy--right-a { top: 69px; }
  .copy--right-b { top: 328px; }
  .copy--right-c { top: 530px; }
  .todo-list { position: absolute; left: 16px; top: 338px; list-style: none; }
  .todo-item {
    display: flex; align-items: center; height: 53px;
    font-family: "Source Sans 3", "Myriad Pro", sans-serif;
    font-weight: 700; font-size: 25px; color: var(--brand-blue);
    letter-spacing: -0.2px; white-space: nowrap;
  }
  .todo-arrow { width: 32px; height: 28px; margin-right: 11px; flex: none; }
  .panel-label {
    position: absolute; top: 815px;
    font-family: "Tinos", "Times New Roman", serif;
    font-size: 78px; line-height: 1; color: var(--label-brown);
    width: 400px; text-align: center;
  }
  .panel-label--one { left: 155px; }
  .panel-label--two { left: 640px; }
</style>
</head>
<body>
<div class="canvas">
  <section class="spread">
    <h2 class="heading heading--mission">Our Mission</h2>
    <p class="copy copy--mission">Our mission plain and simple is to get you seen by a qualified dentist as quickly as possible to get you out of pain. Nobody likes pain and no one should have to live with it. If we can get you seen by a dentist in 24 hours or less, we have succeeded. What we strive for is a quicker, more reliable method for patients to access their dental professional. Going to the local hospitals’ Emergency Department for a tooth ache will not solve the issue, hospitals are often times not equipped to handle dental emergencies and do not have dentists on staff. You leave with antibiotics and pain medication, not a solution to the real underlying problem. Leave here confident, knowing you will see a dentist in less than 24 hours!</p>

    <h2 class="heading heading--todo">What To Do</h2>
    <ul class="todo-list">
      <li class="todo-item"><svg class="todo-arrow" viewBox="0 0 32 28"><polygon points="0,0 32,14 0,28 9,14" fill="var(--brand-blue)"/></svg>Broken or Fractured Filling</li>
      <li class="todo-item"><svg class="todo-arrow" viewBox="0 0 32 28"><polygon points="0,0 32,14 0,28 9,14" fill="var(--brand-blue)"/></svg>Broken or Fractured Tooth</li>
      <li class="todo-item"><svg class="todo-arrow" viewBox="0 0 32 28"><polygon points="0,0 32,14 0,28 9,14" fill="var(--brand-blue)"/></svg>Discolored or Odd Looking Tooth</li>
      <li class="todo-item"><svg class="todo-arrow" viewBox="0 0 32 28"><polygon points="0,0 32,14 0,28 9,14" fill="var(--brand-blue)"/></svg>Just Pain in My Tooth</li>
      <li class="todo-item"><svg class="todo-arrow" viewBox="0 0 32 28"><polygon points="0,0 32,14 0,28 9,14" fill="var(--brand-blue)"/></svg>Loose Tooth</li>
      <li class="todo-item"><svg class="todo-arrow" viewBox="0 0 32 28"><polygon points="0,0 32,14 0,28 9,14" fill="var(--brand-blue)"/></svg>Swelling</li>
    </ul>

    <h2 class="heading heading--right-a">Lorem Isump</h2>
    <p class="copy copy--right copy--right-a">Lorem ipsum dolor sit amet, consectetur adipiscing elit. Ut eget mattis purus. Duis velit lectus, consequat lobortis ultrices a, iaculis ut felis. Nunc condimentum a ipsum ut rutrum. Vestibulum dapibus mollis ultricies. Ut id dolor eget erat placerat interdum nec in nibh. —Lorem IpsumLorem ipsum dolor sit amet, consectetur adipiscing elit. Ut eget mattis purus. Duis velit lectus, consequat lobortis ultrices a, iaculis ut felis. Nunc condimentum a ipsum ut rutrum. Vestibulum dapibus mollis ultricies. Ut id dolor eget erat placerat interdum nec in nibh. —Lorem IpsumLorem ipsum dolor sit amet, consectetur adipiscing elit. Ut eget mattis purus. Duis velit lectus, consequat lobortis ultrices a, iaculis ut felis. Nunc condimentum a ipsum ut rutrum. Vestibulum dapibus mollis ultricies. Ut id dolor eget erat placerat interdum nec in nibh. —Lorem Ipsum</p>

    <h2 class="heading heading--right-b">Lorem Isump</h2>
    <p class="copy copy--right copy--right-b">Lorem ipsum dolor sit amet, consectetur adipiscing elit. Ut eget mattis purus. Duis velit lectus, consequat lobortis ultrices a, iaculis ut felis. Nunc condimentum a ipsum ut rutrum. Vestibulum dapibus mollis ultricies. Ut id dolor eget erat placerat interdum nec in nibh. —Lorem IpsumLorem ipsum dolor sit amet, consectetur adipiscing elit. Ut eget mattis purus. Duis velit lectus, consequat lobortis ultrices a, iaculis ut felis. Nunc condimentum a ipsum ut rutrum. Vestibulum dapibus mollis ultricies. Ut id dolor eget erat placerat interdum nec in nibh. —Lorem IpsumLorem ipsum dolor sit amet, consectetur adipiscing elit. Ut eget mattis purus. Duis velit lectus, consequat lobortis ultrices a, iaculis ut felis. Nunc condimentum a ipsum ut rutrum. Vestibulum dapibus mollis ultricies. Ut id dolor eget erat placerat interdum nec in nibh. —Lorem Ipsum</p>
    <p class="copy copy--right copy--right-c">Lorem ipsum dolor sit amet, consectetur adipiscing elit. Ut eget mattis purus. Duis velit lectus, consequat lobortis ultrices a, iaculis ut felis. Nunc condimentum a ipsum ut rutrum. Vestibulum dapibus mollis ultricies. Ut id dolor eget erat placerat interdum nec in nibh. —Lorem IpsumLorem ipsum dolor sit amet, consectetur adipiscing elit. Ut eget mattis purus. Duis velit lectus, consequat lobortis ultrices a, iaculis ut felis. Nunc condimentum a ipsum ut rutrum. Vestibulum dapibus mollis ultricies. Ut id dolor eget erat placerat interdum nec in nibh. —Lorem IpsumLorem ipsum dolor sit amet, consectetur adipiscing elit. Ut eget mattis purus. Duis velit lectus, consequat lobortis ultrices a, iaculis ut felis. Nunc condimentum a ipsum ut rutrum. Vestibulum dapibus mollis ultricies. Ut id dolor eget erat placerat interdum nec in nibh. —Lorem Ipsum</p>
  </section>

  <div class="panel-label panel-label--one">Inside 1</div>
  <div class="panel-label panel-label--two">Inside 2</div>
</div>
</body>
</html>
```